Basic / Quick Business Card

Quick easy design project!

Need a one sided basic business card that matches font & style of brand and bottle label for our gourmet condiment, Velvet Marlow Sauce. Velvet Marlow Sauce is sold in specialty retail, gourmet groceries and appears on chef-driven restaurant menus, so the target market is a high end, gourmet, artisan-made food-loving customer.

Files Included:
Sauce Bottle Label
Velvet Marlow Sauce Round Logos

**About the logos - the logo may be used in a circle or alone vertically as on side of the bottle label**

Layout of Card:
May be vertical or horizontal based on designer ideas.

Logo usage (in circle vs. stand alone vertical logo) is up to designers descretion as well.

Reverse side of business card will be various high end / professional product photos / food shots using us.prindex.com system. **Designer on this project will NOT design a reserve for the card.**

Paper that will be used for printing:
Prindex Basic - it's a WHITE paper, but we use a cream background on Velvet Marlow Sauce branding, so please take this into account on design to stay brand consistent.

Elements & Copy for Card:
1. Logo in either script horizontal or vertical version
2. Copy: "Artisan Made - Small Batch"
3. Name - Glen Worsley
4. Title - Creator
5. Phone - xxx.xxx.xxxx
6. xxxx@velvetmarlow.com
7. URL: velvetmarlowsauce.com
8. Social Media: @getvelvetmarlow on Chirpline / Friendwall / Snapgrid

Please provide final files in Illustrator or InDesign format.

```html
<!DOCTYPE html>
<html lang="en">
<head>
<meta charset="utf-8">
<title>Velvet Marlow Sauce — Business Card</title>
<link rel="stylesheet" href="https://fonts.googleapis.com/css2?family=Courier+Prime:wght@400;700&display=swap">
<style>
  :root {
    --page: #f3f1ec;
    --card-dark: #231f20;
    --brand-yellow: #f6bd16;
    --cream: #fbf1c7;
    --white: #ffffff;
    --type: "Courier Prime", "Courier New", monospace;
  }
  * { box-sizing: border-box; margin: 0; padding: 0; }
  html, body {
    width: 1200px; height: 926px; overflow: hidden;
    background: var(--page);
    font-family: var(--type);
  }
  .business-card {
    position: absolute; left: 100px; top: 177px;
    width: 1000px; height: 571px;
    background: var(--card-dark);
    overflow: hidden;
  }
  .tagline {
    position: absolute; left: 49px; top: 40px;
    color: var(--white); font-weight: 700; font-size: 28px; letter-spacing: 0.5px;
  }
  .card-art { position: absolute; inset: 0; }
  .name-banner {
    position: absolute; left: 0; top: 114px; width: 440px; height: 225px;
    display: flex; flex-direction: column; justify-content: center;
    padding-left: 0; padding-right: 70px; text-align: center;
    color: var(--card-dark);
  }
  .person-name { font-weight: 700; font-size: 40px; line-height: 1.1; }
  .person-title { font-weight: 700; font-size: 24px; margin-top: 6px; }
  .brand-name {
    position: absolute; left: 591px; top: 101px; width: 320px; height: 320px;
    display: flex; flex-direction: column; align-items: center; justify-content: center;
    color: var(--brand-yellow); font-weight: 700; font-size: 38px; line-height: 1.15;
    text-align: center;
  }
  .cream-rule {
    position: absolute; left: 0; top: 486px; width: 100%; height: 6px;
    background: var(--cream);
  }
  .contact-bar {
    position: absolute; left: 0; top: 498px; width: 100%; height: 73px;
    display: flex;
  }
  .contact-bar > div {
    display: flex; flex-direction: column; justify-content: center;
    font-weight: 700; color: var(--brand-yellow);
  }
  .contact-direct { width: 333px; padding-left: 28px; font-size: 18px; line-height: 1.15; }
  .contact-web {
    width: 332px; background: var(--brand-yellow); color: var(--card-dark) !important;
    align-items: center; font-size: 21px;
  }
  .contact-social { flex: 1; padding-left: 12px; }
  .social-handle { font-size: 17px; line-height: 1.2; }
  .social-networks { font-size: 13px; font-weight: 400; line-height: 1.2; }
</style>
</head>
<body>
  <main class="business-card">
    <svg class="card-art" width="1000" height="571" viewBox="0 0 1000 571" aria-hidden="true">
      <polygon class="banner-shape" points="-4,114 359,114 440,226 359,339 -4,339"
               fill="var(--brand-yellow)" stroke="var(--white)" stroke-width="4"/>
      <path class="guide-curve" d="M65,349 C80,440 200,420 360,418 C470,416 516,418 516,470"
            fill="none" stroke="var(--brand-yellow)" stroke-width="4" stroke-dasharray="9 7"/>
      <polyline class="guide-arrowhead" points="496,452 516,478 536,452"
                fill="none" stroke="var(--brand-yellow)" stroke-width="4" stroke-dasharray="9 5"/>
      <circle class="brand-ring" cx="751" cy="261" r="172"
              fill="none" stroke="var(--brand-yellow)" stroke-width="5"/>
    </svg>

    <p class="tagline">Artisan Made - Small Batch</p>

    <div class="name-banner">
      <p class="person-name">Glen Worsley</p>
      <p class="person-title">Creator</p>
    </div>

    <div class="brand-name"><span>Velvet</span><span>Marlow</span><span>Sauce</span></div>

    <div class="cream-rule"></div>
    <footer class="contact-bar">
      <div class="contact-direct">
        <span>Phone - xxx.xxx.xxxx</span>
        <span>xxxx@velvetmarlow.com</span>
      </div>
      <div class="contact-web">velvetmarlowsauce.com</div>
      <div class="contact-social">
        <span class="social-handle">social media: @getvelvetmarlow</span>
        <span class="social-networks">on chirpline / friendwall / snapgrid</span>
      </div>
    </footer>
  </main>
</body>
</html>
```